Haunted Attraction Expert Website Design

A complete professional looking web site with 6 total pages.
Includes calendar and email form.
Needs to be word press and mobile user friendly.
Please use photos as labeled for the pages they will be presented on.
Company logo should alternate left and right sides of the page.
See attached layout for directions

Target Market(s)

Professionals, Haunted Attraction Owners/Operators

Industry/Entity Type

It Professional

Coding

Coded - Design and coding required

Number of Pages Required

5+ page

Font styles to use
Sans Serif

Colors

Designer to choose colors to be used in the design.

Requirements
Must have
• Our company logo on each page and photos supplied by me assigned to specific pages.
• Calendar
• Contact US Email Submission Form

```html
<!DOCTYPE html>
<html lang="en">
<head>
<meta charset="utf-8">
<title>Fright Venue Advisors</title>
<link rel="stylesheet" href="https://fonts.googleapis.com/css2?family=Lato:ital,wght@0,400;0,700;0,900;1,400&family=Oswald:wght@400;500;600&display=swap">
<style>
:root{
  --orange:#f7a21b;
  --ink:#2b2b2b;
  --text:#4a4a4a;
  --muted:#8a8a8a;
  --light:#f3f3f3;
  --white:#ffffff;
  --footer:#232323;
  --footer-text:#9a9a9a;
  --cal-head:#9c9c9c;
  --cal-line:#d9d9d9;
  --cal-tab:#3a3a3a;
}
*{box-sizing:border-box;margin:0;padding:0}
html,body{width:1200px;height:2542px;overflow:hidden;background:var(--white)}
body{font-family:'Lato',sans-serif;color:var(--text);position:relative}
.page{position:relative;width:1200px;height:2542px;overflow:hidden}

/* header */
.site-header{position:absolute;left:0;top:0;width:1200px;height:86px;background:var(--white)}
.brand{position:absolute;left:75px;top:20px;display:flex;align-items:center;gap:12px}
.brand-square{width:44px;height:44px;background:var(--orange)}
.brand-name{font-family:'Oswald',sans-serif;font-weight:500;font-size:24px;line-height:26px;color:var(--ink);width:200px}
.main-nav{position:absolute;right:72px;top:38px;display:flex;gap:30px}
.main-nav a{font-family:'Lato',sans-serif;font-weight:700;font-size:13px;color:var(--ink);text-decoration:none;letter-spacing:.3px}
.main-nav a.active{color:var(--orange)}

/* hero */
.hero{position:absolute;left:0;top:86px;width:1200px;height:575px;background:linear-gradient(110deg,#3d4148 0%,#5d6169 35%,#a54a22 55%,#6a6e74 75%,#9aa0a6 100%)}
.hero-box{position:absolute;left:75px;top:172px;width:462px;height:254px;background:rgba(25,25,25,.72);padding:22px 20px}
.hero-title{font-family:'Oswald',sans-serif;font-weight:500;font-size:46px;line-height:50px;color:var(--white);letter-spacing:.5px}
.hero-text{margin-top:10px;font-size:19px;line-height:29px;color:var(--white)}

/* welcome */
.welcome{position:absolute;left:0;top:661px;width:1200px;height:698px;background:var(--white)}
.welcome h2{position:absolute;left:0;top:52px;width:1200px;text-align:center;font-family:'Lato',sans-serif;font-weight:900;font-size:28px;color:var(--ink);letter-spacing:.5px}
.welcome-text{position:absolute;left:80px;top:102px;width:1040px;text-align:center;font-size:13.5px;line-height:23px;color:var(--text)}
.welcome-text p+p{margin-top:23px}
.service{position:absolute;width:260px;text-align:center}
.service-ring{width:80px;height:80px;border:2px solid var(--orange);border-radius:50%;margin:0 auto;display:flex;align-items:center;justify-content:center}
.service-ring svg{width:30px;height:30px;fill:var(--ink)}
.service-name{margin-top:12px;font-weight:700;font-size:16px;line-height:21px;color:var(--ink)}
.service-name.single{margin-top:22px}
.welcome-note{position:absolute;left:0;top:624px;width:1200px;text-align:center;font-size:14px;color:var(--text)}

/* photo band */
.photo-band{position:absolute;left:0;top:1359px;width:1200px;height:446px;background:radial-gradient(ellipse at 55% 45%,#5a4a3e 0%,#2f2620 45%,#141110 100%)}

/* info */
.info{position:absolute;left:0;top:1805px;width:1200px;height:509px;background:var(--light)}
.profile-card{position:absolute;left:75px;top:65px;width:330px;height:381px;background:var(--white);text-align:center}
.profile-photo{width:180px;height:180px;border-radius:50%;margin:20px auto 0;background:radial-gradient(circle at 50% 40%,#c9b9ac 0%,#8d8a8c 55%,#4b4e54 100%)}
.profile-quote{margin-top:22px;font-style:italic;font-size:17px;line-height:26px;color:var(--text)}
.profile-author{margin-top:4px;font-weight:700;font-size:14px;color:var(--orange)}
.profile-brand{margin:22px auto 0;display:flex;justify-content:center;align-items:center;gap:8px}
.profile-brand .sq{width:20px;height:20px;background:var(--orange)}
.profile-brand .nm{font-family:'Lato',sans-serif;font-weight:700;font-size:20px;color:var(--ink)}
.calendar-card{position:absolute;left:434px;top:65px;width:691px;height:381px;background:var(--white)}
.calendar-card h3{position:absolute;left:0;top:26px;width:691px;text-align:center;font-weight:900;font-size:28px;color:var(--ink)}
.calendar{position:absolute;left:27px;top:79px;width:642px;border:1px solid var(--cal-line)}
.cal-bar{position:relative;height:34px;background:var(--orange)}
.cal-month{position:absolute;left:0;top:0;height:34px;width:175px;background:var(--cal-tab);clip-path:polygon(0 0,100% 0,88% 100%,0 100%);color:var(--white);font-weight:700;font-size:13px;line-height:34px;padding-left:28px}
.cal-arrows{position:absolute;right:14px;top:9px;display:flex;gap:8px}
.cal-arrows svg{width:10px;height:14px;stroke:var(--white);stroke-width:2;fill:none}
.cal-grid{display:grid;grid-template-columns:repeat(7,1fr)}
.cal-grid span{height:41px;border-right:1px solid var(--cal-line);border-bottom:1px solid var(--cal-line);display:flex;align-items:center;justify-content:center;font-size:14px;color:var(--ink)}
.cal-grid span:nth-child(7n){border-right:none}
.cal-grid .dow{height:34px;background:var(--cal-head);color:var(--white);font-weight:700;border-color:#b5b5b5}
.cal-grid span.last{border-bottom:none}

/* footer */
.site-footer{position:absolute;left:0;top:2314px;width:1200px;height:228px;background:var(--footer)}
.footer-brand{position:absolute;left:75px;top:60px;display:flex;align-items:center;gap:10px}
.footer-brand .sq{width:36px;height:36px;background:var(--orange)}
.footer-brand .nm{font-family:'Oswald',sans-serif;font-weight:500;font-size:20px;line-height:22px;color:#7a7a7a;width:170px}
.copyright{position:absolute;left:75px;top:126px;font-size:12px;line-height:20px;color:#6f6f6f}
.footer-title{position:absolute;top:62px;font-weight:900;font-size:13px;color:var(--white);letter-spacing:.4px}
.sitemap{position:absolute;left:350px;top:94px;display:grid;grid-template-columns:108px 130px;row-gap:14px}
.sitemap a{font-size:12.5px;color:#cfcfcf;text-decoration:none}
.email-field{position:absolute;left:636px;top:96px;width:232px;height:38px;background:var(--white);border:none;border-radius:2px;padding-left:12px;font-family:'Lato',sans-serif;font-size:12.5px;color:var(--ink)}
.email-field::placeholder{color:var(--ink)}
.email-button{position:absolute;left:791px;top:139px;width:78px;height:33px;background:var(--orange);color:var(--white);border:none;border-radius:2px;font-family:'Lato',sans-serif;font-weight:900;font-size:12px;letter-spacing:.5px}
.social{position:absolute;left:929px;top:96px;display:flex;gap:12px}
.social span{width:17px;height:17px;border-radius:50%;background:var(--white)}
</style>
</head>
<body>
<div class="page">

  <header class="site-header">
    <div class="brand"><div class="brand-square"></div><div class="brand-name">Fright Venue Advisors</div></div>
    <nav class="main-nav">
      <a class="active" href="#">HOME</a>
      <a href="#">ABOUT</a>
      <a href="#">CONSULTING</a>
      <a href="#">EXPERT WITNESSES</a>
      <a href="#">UPCOMING EVENTS</a>
      <a href="#">CONTACT US</a>
    </nav>
  </header>

  <section class="hero" role="img" aria-label="Firefighters in protective gear spraying water at a burning vehicle">
    <div class="hero-box">
      <h1 class="hero-title">FRIGHT VENUE<br>ADVISORS</h1>
      <p class="hero-text">Fright Venue Advisors FVA provides UBSC Unified Building Safety Code, as well as NSFA National Safety &amp; Fire Association Code Compliance Safety Training.</p>
    </div>
  </section>

  <section class="welcome">
    <h2>WELCOME TO OUR WEBSITE</h2>
    <div class="welcome-text">
      <p>Fright Venue Advisors FVA provides UBSC Unified Building Safety Code, as well as NSFA National Safety &amp; Fire Association Code Compliance Safety Training. Consulting services that cover all aspects of owning and operating a Haunted Attraction, to include Design, Construction, Staff Training, Safety, Security and Operations.</p>
      <p>Fright Venue Advisors also provides Experienced Witness and Litigation Consulting Services for Safety related legal matters within the Haunted Attraction Industry; cases that involve, fatalities, catastrophic and personal injuries and Haunted Attraction Safety</p>
    </div>

    <div class="service" style="left:67px;top:284px">
      <div class="service-ring"><svg viewBox="0 0 24 24"><path d="M5 2h10l5 5v15H5z M14 2v6h6" /><rect x="8" y="11" width="9" height="1.6" fill="#fff"/><rect x="8" y="14" width="9" height="1.6" fill="#fff"/><rect x="8" y="17" width="6" height="1.6" fill="#fff"/></svg></div>
      <div class="service-name">Accident /<br>Incident Investigation</div>
    </div>
    <div class="service" style="left:336px;top:284px">
      <div class="service-ring"><svg viewBox="0 0 24 24"><path d="M10 2a8 8 0 0 1 6.3 12.9l5.4 5.4-2 2-5.4-5.4A8 8 0 1 1 10 2zm0 3a5 5 0 1 0 0 10 5 5 0 0 0 0-10z"/></svg></div>
      <div class="service-name single">Attraction Inspections</div>
    </div>
    <div class="service" style="left:606px;top:284px">
      <div class="service-ring"><svg viewBox="0 0 24 24"><path d="M4 5h16v10H4z M6 7v6h12V7z M1 17h22v2H1z"/></svg></div>
      <div class="service-name">Crisis Management<br>Training</div>
    </div>
    <div class="service" style="left:875px;top:284px">
      <div class="service-ring"><svg viewBox="0 0 24 24"><circle cx="12" cy="7" r="5"/><path d="M3 22c0-5 4-8 9-8s9 3 9 8z"/></svg></div>
      <div class="service-name single">Expert Witness</div>
    </div>

    <div class="service" style="left:67px;top:445px">
      <div class="service-ring"><svg viewBox="0 0 24 24"><path d="M12 1l6 6h-4v4h7v12H3V11h7V7H6z"/></svg></div>
      <div class="service-name">Haunted Attraction<br>Construction</div>
    </div>
    <div class="service" style="left:336px;top:445px">
      <div class="service-ring"><svg viewBox="0 0 24 24"><ellipse cx="10" cy="9" rx="8" ry="6"/><path d="M5 13l-2 5 6-3z"/><path d="M19 9.5c2.5 1 4 3 4 5 0 1.8-1 3.3-2.5 4.3l1.5 3.2-4.5-2.2c-.5.1-1 .2-1.5.2-3 0-5.5-1.5-6.5-3.5 5 0 9.5-3 9.5-7z"/></svg></div>
      <div class="service-name single">Litigation Consulting</div>
    </div>
    <div class="service" style="left:606px;top:445px">
      <div class="service-ring"><svg viewBox="0 0 24 24"><path d="M9 2h14v11H9z" fill="none" stroke="#2b2b2b" stroke-width="1.6"/><circle cx="5" cy="6" r="2.4"/><path d="M2 9h5l5 2v1.6l-4-1V16H3z"/><circle cx="5" cy="19" r="1.8"/><circle cx="12" cy="19" r="1.8"/><circle cx="19" cy="19" r="1.8"/><path d="M2 24c0-2 1.4-3 3-3s3 1 3 3zm7 0c0-2 1.4-3 3-3s3 1 3 3zm7 0c0-2 1.4-3 3-3s3 1 3 3z"/></svg></div>
      <div class="service-name single">Safety Training</div>
    </div>
    <div class="service" style="left:875px;top:445px">
      <div class="service-ring"><svg viewBox="0 0 24 24"><circle cx="12" cy="7" r="3.6"/><circle cx="5" cy="9" r="2.6"/><circle cx="19" cy="9" r="2.6"/><path d="M6 20c0-4 2.7-7 6-7s6 3 6 7z"/><path d="M0 19c0-3 2-5 5-5 1 0 1.5.2 2 .5-1.2 1.3-2 3-2 4.5z"/><path d="M24 19c0-3-2-5-5-5-1 0-1.5.2-2 .5 1.2 1.3 2 3 2 4.5z"/></svg></div>
      <div class="service-name single">Staff Training</div>
    </div>

    <p class="welcome-note">For Haunted Houses, Haunted Woods, Corn Mazes and Hay Rides.</p>
  </section>

  <section class="photo-band" role="img" aria-label="Costumed haunted attraction actors in a dim rustic workshop set"></section>

  <section class="info">
    <div class="profile-card">
      <div class="profile-photo" role="img" aria-label="Portrait of the company founder"></div>
      <p class="profile-quote">“Do what is right, not what is easy,<br>nor what is popular.”</p>
      <p class="profile-author">Dale M Harlow</p>
      <div class="profile-brand"><span class="sq"></span><span class="nm">FVA</span></div>
    </div>

    <div class="calendar-card">
      <h3>EVENT CALENDAR</h3>
      <div class="calendar">
        <div class="cal-bar">
          <div class="cal-month">JANUARY 2018</div>
          <div class="cal-arrows">
            <svg viewBox="0 0 10 14"><path d="M7 2L3 7l4 5"/></svg>
            <svg viewBox="0 0 10 14"><path d="M3 2l4 5-4 5"/></svg>
          </div>
        </div>
        <div class="cal-grid">
          <span class="dow">S</span><span class="dow">M</span><span class="dow">T</span><span class="dow">W</span><span class="dow">T</span><span class="dow">F</span><span class="dow">S</span>
          <span></span><span>1</span><span>2</span><span>3</span><span>4</span><span>5</span><span>6</span>
          <span>7</span><span>8</span><span>9</span><span>10</span><span>11</span><span>12</span><span>13</span>
          <span>14</span><span>15</span><span>16</span><span>17</span><span>18</span><span>19</span><span>20</span>
          <span>21</span><span>22</span><span>23</span><span>24</span><span>25</span><span>26</span><span>27</span>
          <span class="last">28</span><span class="last">29</span><span class="last">30</span><span class="last">31</span><span class="last"></span><span class="last"></span><span class="last"></span>
        </div>
      </div>
    </div>
  </section>

  <footer class="site-footer">
    <div class="footer-brand"><span class="sq"></span><span class="nm">Fright Venue Advisors</span></div>
    <p class="copyright">Copyright © 2018. Company Name<br>All Right Reserved</p>

    <h4 class="footer-title" style="left:350px">SITE MAP</h4>
    <nav class="sitemap">
      <a href="#">Home</a><a href="#">Expert Witnesses</a>
      <a href="#">About</a><a href="#">Upcoming Events</a>
      <a href="#">Consulting</a><a href="#">Contact Us</a>
    </nav>

    <h4 class="footer-title" style="left:636px">EMAIL SUBSCRIBE</h4>
    <input class="email-field" type="email" placeholder="Enter Email">
    <button class="email-button" type="button">SIGN UP</button>

    <h4 class="footer-title" style="left:929px">FOLLOW US</h4>
    <div class="social" aria-label="Social links"><span></span><span></span><span></span><span></span><span></span></div>
  </footer>

</div>
</body>
</html>
```